Business card design needed for Pollen Bakes

We need a new business card designed for our business. We create complete DIY cake kits to be delivered Australia Wide.

I would like our logo used (see attached).

Industry/Entity Type

Business

Contact Information for Business Card

Pollen Bakes - Complete DIY Cake Kits
www.pollenbakes.com.au
0472 315 904
sales@pollenbakes.com.au
www.facebook.com/pollenbakes1

Requirements
Must have
• logo

```html
<!DOCTYPE html>
<html lang="en">
<head>
<meta charset="UTF-8">
<title>Pollen Bakes – Business Card</title>
<link href="https://fonts.googleapis.com/css2?family=Andika:wght@400;700&display=swap" rel="stylesheet">
<style>
  :root {
    --card-bg-light: #d6e6df;
    --card-bg-mid: #b6d2c9;
    --card-bg-deep: #9cbfb4;
    --brand-red: #c8202c;
    --ink: #111111;
    --band-cream: #f3e6c2;
    --band-edge: #e0cb94;
    --twine: #a9854c;
    --tag-cream: #f3ddae;
    --tag-warm: #e9c98f;
  }
  html, body {
    margin: 0;
    padding: 0;
    overflow: hidden;
    background: #ffffff;
  }
  .card {
    position: relative;
    width: 1200px;
    height: 693px;
    overflow: hidden;
    font-family: "Andika", "Trebuchet MS", sans-serif;
  }
  .dotted-backdrop {
    position: absolute;
    inset: 0;
    background: radial-gradient(ellipse at 30% 60%, var(--card-bg-light) 0%, var(--card-bg-mid) 60%, var(--card-bg-deep) 100%);
  }
  .ribbon-band {
    position: absolute;
    left: 0;
    top: 0;
    width: 1200px;
    height: 112px;
    background: linear-gradient(180deg, var(--band-cream) 0%, var(--band-cream) 75%, var(--band-edge) 100%);
  }
  .twine {
    position: absolute;
    left: 0;
    top: 0;
    width: 1200px;
    height: 693px;
  }
  .cupcake-tag {
    position: absolute;
    left: 848px;
    top: 228px;
    width: 338px;
    height: 452px;
    border-radius: 70px;
    background: radial-gradient(ellipse at 50% 50%, var(--tag-cream) 0%, var(--tag-cream) 55%, var(--tag-warm) 100%);
  }
  .brand-name {
    position: absolute;
    left: 44px;
    top: 24px;
    margin: 0;
    color: var(--brand-red);
    font-weight: 700;
    font-size: 140px;
    line-height: 146px;
  }
  .brand-name .line { display: block; }
  .brand-name .line-second { padding-left: 90px; }
  .tagline {
    position: absolute;
    left: 204px;
    top: 312px;
    margin: 0;
    color: var(--brand-red);
    font-size: 45px;
    font-weight: 400;
    line-height: 52px;
  }
  .contact-list {
    position: absolute;
    left: 34px;
    top: 440px;
    margin: 0;
    padding: 0;
    list-style: none;
    color: var(--ink);
    font-size: 54px;
    line-height: 52px;
  }
</style>
</head>
<body>
  <main class="card">
    <div class="dotted-backdrop" role="img" aria-label="Soft sea-green background with white polka dots"></div>
    <div class="ribbon-band" role="img" aria-label="Cream lace ribbon band with a twine bow across the top edge"></div>

    <svg class="twine" viewBox="0 0 1200 693" aria-hidden="true">
      <path d="M 1057 48 L 975 240" stroke="var(--twine)" stroke-width="4" fill="none"/>
      <path d="M 1057 48 L 1070 240" stroke="var(--twine)" stroke-width="4" fill="none"/>
    </svg>

    <div class="cupcake-tag" role="img" aria-label="Cream scalloped label showing a cupcake with pink icing and a cherry"></div>

    <h1 class="brand-name">
      <span class="line">Pollen</span>
      <span class="line line-second">Bakes</span>
    </h1>
    <p class="tagline">Complete DIY Cake Kits</p>

    <ul class="contact-list">
      <li>sales@pollenbakes.com.au</li>
      <li>tel. (0472) 315 - 904</li>
      <li>www.pollenbakes.com.au</li>
      <li>www.facebook.com/pollenbakes1</li>
    </ul>
  </main>
</body>
</html>
```